Vesk Architecture

We are a architectural design and build company working between scales 1/1000 to 1/1 we want people to understand our difference from our design experience and quality.we build hotels restourants and office spaces.Our company name is Vesk architecture to mind sustainability.

We want to write our adress phone and work spesifications on the card and we want our logo as backround.

Ps:you could find the logo adress and phone box numbers from the web:www.veskmimarlik-ornek.com

Target Market(s)

Who looks for experts.

Industry/Entity Type

Architecture

Requirements
Must have
• Design is over everything.
Should not have
• we don want it to be colorfull

```html
<!DOCTYPE html>
<html lang="tr">
<head>
<meta charset="utf-8">
<title>Vesk Mimarlık — Kartvizit</title>
<link rel="stylesheet" href="https://fonts.googleapis.com/css2?family=Barlow:wght@300;400;500&display=swap">
<style>
  :root {
    --page-bg: #dcdcdc;
    --card-light: #6b6b6b;
    --card-mid: #4a4a4a;
    --card-dark: #2c2c2c;
    --ink: #ffffff;
    --ink-soft: #e4e4e4;
    --shadow: rgba(0, 0, 0, 0.28);
  }
  * { margin: 0; padding: 0; box-sizing: border-box; }
  html, body {
    width: 900px;
    height: 1200px;
    overflow: hidden;
    background: var(--page-bg);
    font-family: "Barlow", "Helvetica Neue", Arial, sans-serif;
    color: var(--ink);
  }
  .canvas {
    position: relative;
    width: 900px;
    height: 1200px;
  }
  .card {
    position: absolute;
    left: 153px;
    width: 620px;
    height: 400px;
    background: radial-gradient(ellipse 62% 70% at 50% 50%, var(--card-light) 0%, var(--card-mid) 50%, var(--card-dark) 100%);
    box-shadow: 0 6px 18px var(--shadow);
    overflow: hidden;
  }
  .card--front { top: 144px; }
  .card--back  { top: 657px; }

  /* Front side */
  .wordmark {
    position: absolute;
    font-weight: 500;
    color: var(--ink);
    line-height: 1;
  }
  .card--front .wordmark {
    left: 80px;
    top: 66px;
  }
  .wordmark__name {
    display: block;
    font-size: 86px;
    letter-spacing: 2px;
    text-transform: lowercase;
  }
  .wordmark__sub {
    display: block;
    font-size: 20px;
    letter-spacing: 3px;
    margin-top: 6px;
  }
  .contact-person {
    position: absolute;
    left: 356px;
    top: 128px;
    width: 170px;
    text-align: center;
  }
  .contact-person__name {
    font-size: 17px;
    font-weight: 300;
    letter-spacing: 0.5px;
  }
  .contact-person__role {
    font-size: 14px;
    font-weight: 300;
    color: var(--ink-soft);
    margin-top: 3px;
  }
  .contact-details {
    position: absolute;
    left: 293px;
    top: 262px;
    font-size: 15.5px;
    font-weight: 300;
    line-height: 23px;
    color: var(--ink-soft);
    list-style: none;
  }
  .contact-details__label {
    display: inline-block;
    width: 16px;
  }

  /* Back side */
  .card--back .wordmark {
    left: 0;
    right: 0;
    top: 108px;
    text-align: center;
  }
  .card--back .wordmark__name {
    font-size: 150px;
    letter-spacing: 4px;
  }
  .card--back .wordmark__sub {
    font-size: 32px;
    letter-spacing: 5px;
    margin-top: 10px;
  }
</style>
</head>
<body>
<main class="canvas">
  <section class="card card--front" aria-label="Kartvizit ön yüz">
    <div class="wordmark">
      <span class="wordmark__name">Vesk</span>
      <span class="wordmark__sub">MİMARLIK</span>
    </div>
    <div class="contact-person">
      <p class="contact-person__name">Deniz Arman YALÇIN</p>
      <p class="contact-person__role">Mimar</p>
    </div>
    <ul class="contact-details">
      <li>Bahariye Mah. Ilgın Cad. Sedef Sok.</li>
      <li>No:7 Kadıköy / İSTANBUL</li>
      <li><span class="contact-details__label">t.</span> 0216 555 01 47</li>
      <li><span class="contact-details__label">f.</span> 0216 555 01 48</li>
      <li><span class="contact-details__label">e.</span> veskmimarlik@ornekposta.com</li>
    </ul>
  </section>

  <section class="card card--back" aria-label="Kartvizit arka yüz">
    <div class="wordmark">
      <span class="wordmark__name">Vesk</span>
      <span class="wordmark__sub">MİMARLIK</span>
    </div>
  </section>
</main>
</body>
</html>
```